Create a flyer for Pressure Washing: Harborline Pressure Washing

looking to create a 4 page booklet (8.5'x11") flyer to market my power washing company. Promote before and after pictures; the services i provide and to get a quote today.
Company name: Harborline Pressure Washing

Boost Your Home’s Curb Appeal
Services:
• Residential & Commercial Washing
• Driveways, Sidewalks & Concrete Cleaning
• Decks, Patios & Paver Restoration
• Tennis Courts & Specialty Surface Cleaning

Benefits:
✔ Boost curb appeal instantly
✔ Remove mold, algae, and dirt
✔ Protect your property surfaces
✔ Improve property value

Target Market(s)

mailer flyers to 500+ homes in New Jersey & NY

Industry/Entity Type

pressure washing

Font styles to use
Sans Serif

Colors
0054AA
0677BA
7BADD7
CADEEF
E8F1F8

Requirements
Must have
• 4 page booklet of before and after images, a cohesive design and helpful call to actions

```html
<!DOCTYPE html>
<html lang="en">
<head>
<meta charset="utf-8">
<title>Harborline Pressure Washing – Booklet</title>
<link rel="stylesheet" href="https://fonts.googleapis.com/css2?family=Oswald:wght@600;700&family=Poppins:ital,wght@0,400;0,600;0,700;1,800&display=swap">
<style>
:root{
  --navy:#0a1a5c;
  --blue:#0054aa;
  --blue-mid:#0677ba;
  --blue-deep:#1e46a8;
  --sky:#7badd7;
  --mist:#cadeef;
  --ice:#e8f1f8;
  --white:#ffffff;
  --ink:#0d1b3a;
  --yellow:#f2b51c;
  --red:#e03131;
  --green:#2b9a3e;
}
*{box-sizing:border-box;margin:0;padding:0}
html,body{width:891px;height:1200px;overflow:hidden}
body{background:var(--navy);font-family:"Poppins",sans-serif;color:var(--ink);position:relative}
.spread{position:absolute;display:flex;box-shadow:0 14px 30px rgba(0,0,0,.45)}
.spread--cover{left:163px;top:105px;width:524px;height:435px}
.spread--services{left:163px;top:690px;width:567px;height:435px}
.page{position:relative;flex:1;overflow:hidden;background:var(--white)}
.headline{font-family:"Oswald",sans-serif;font-weight:700;text-transform:uppercase;line-height:1.05}
.photo{position:absolute}
.brand{position:absolute;border-radius:50%;border:2px solid var(--ink);background:var(--white);display:flex;align-items:center;justify-content:center;text-align:center;font-family:"Poppins",sans-serif;font-weight:700;font-size:5px;line-height:1.15;color:var(--ink);padding:3px}

/* ---------- back cover ---------- */
.back{background:linear-gradient(90deg,var(--white) 0%,var(--ice) 80%,#d3dbe6 100%)}
.back__blob{position:absolute;left:-40px;top:-60px;width:200px;height:130px;border-radius:0 0 120px 0;background:var(--mist)}
.back__arcs{position:absolute;left:0;top:40px}
.benefits{position:absolute;left:78px;top:112px;width:170px;color:var(--white)}
.benefits__title{font-family:"Poppins",sans-serif;font-weight:700;font-size:16px;letter-spacing:.5px;margin:0 0 8px 14px}
.benefits__list{list-style:none;font-size:8.6px;font-weight:600}
.benefits__list li{display:flex;align-items:center;gap:5px;margin-bottom:8px}
.tick{width:10px;height:10px;flex:none}
.back__cta{position:absolute;left:24px;top:309px;width:134px;height:21px;border-radius:3px;background:var(--blue-deep);color:var(--white);font-size:8px;font-weight:600;display:flex;align-items:center;justify-content:center}
.back__tagline{position:absolute;left:24px;top:337px;font-size:10px;font-weight:800;font-style:italic;color:var(--ink)}
.back__phone{position:absolute;left:24px;top:365px;width:137px;height:42px;border-radius:3px;background:var(--mist);display:flex;align-items:center;gap:12px;padding-left:12px;font-size:11px;font-weight:600;color:var(--ink)}
.back__phone svg{width:14px;height:14px}
.back .brand{left:210px;top:363px;width:48px;height:48px}

/* ---------- front cover ---------- */
.front{background:linear-gradient(90deg,#dfe5ee 0%,var(--white) 12%)}
.front__title{position:absolute;left:20px;top:20px;font-size:17px;color:var(--ink);width:180px}
.front__rule{position:absolute;left:20px;top:66px;width:74px;height:4px;background:var(--yellow)}
.front .brand{left:199px;top:22px;width:56px;height:56px}
.before-after{left:18px;top:82px;width:244px;height:166px;display:flex}
.before-after__half{flex:1;position:relative}
.before-after__half--before{background:linear-gradient(180deg,#6f8a5a 0%,#c9c6bd 35%,#8d8a80 100%)}
.before-after__half--after{background:linear-gradient(180deg,#6f8a5a 0%,#d6d2c8 35%,#a7704f 100%)}
.tag{position:absolute;bottom:4px;left:50%;transform:translateX(-50%);background:var(--white);font-size:8px;font-weight:700;padding:2px 12px;border-radius:2px}
.tag--before{color:var(--red)}
.tag--after{color:var(--green)}
.front__panel{position:absolute;left:18px;top:248px;right:0;height:166px;background:var(--blue-deep);color:var(--white);padding:28px 0 0 24px}
.front__panel-title{font-size:15px;width:190px}
.front__panel-text{font-size:5.6px;width:170px;margin-top:6px;line-height:1.45}
.front__button{position:absolute;left:24px;top:107px;width:116px;height:24px;border-radius:3px;background:var(--white);color:var(--blue-deep);font-size:8px;font-weight:600;display:flex;align-items:center;justify-content:center}
.front__stripes{position:absolute;right:0;bottom:0}

/* ---------- services inside ---------- */
.services{background:linear-gradient(90deg,var(--white) 0%,var(--ice) 85%,#cfd6e1 100%);padding:28px 18px 0 21px}
.services__title{font-family:"Poppins",sans-serif;font-weight:700;font-size:15px;color:var(--ink)}
.services__intro{font-size:5.8px;line-height:1.5;margin-top:8px;width:240px}
.service{position:absolute;left:21px;width:245px;display:flex;gap:14px}
.service__photo{position:static;width:78px;height:63px;border:3px solid var(--yellow);flex:none}
.service__name{font-size:7.2px;font-weight:700;text-transform:uppercase;margin-top:8px;line-height:1.3}
.service__text{font-size:5.5px;line-height:1.5;margin-top:5px}
.service__rule{position:absolute;left:114px;width:150px;height:2px;background:var(--blue-deep)}

/* ---------- features inside ---------- */
.features{background:var(--white)}
.feature{position:absolute;left:0;right:0}
.feature--driveway{top:0;height:137px;background:linear-gradient(90deg,var(--blue) 0%,var(--blue-deep) 55%,var(--white) 55%)}
.feature--deck{top:140px;height:158px;background:linear-gradient(90deg,var(--ice) 0%,var(--white) 40%,var(--yellow) 40%)}
.feature--concrete{top:302px;height:133px;background:linear-gradient(90deg,var(--blue) 0%,var(--blue-deep) 55%,var(--white) 55%)}
.feature__label{position:absolute;font-size:15px;color:var(--white);width:100px}
.feature__photo{border:3px solid var(--yellow)}
.feature--driveway .feature__photo{left:117px;top:12px;width:166px;height:116px;background:linear-gradient(180deg,#9fb8cc 0%,#7f9a6a 35%,#bfc3c2 55%,#7c7a6e 100%)}
.feature--concrete .feature__photo{left:117px;top:6px;width:166px;height:123px;background:linear-gradient(180deg,#6b8360 0%,#a5a69f 40%,#d9dad7 100%)}
.deck__ring{position:absolute;left:-12px;top:13px;width:132px;height:132px;border-radius:50%;border:10px solid var(--blue-deep);background:var(--white)}
.deck__photo{position:absolute;left:0;top:25px;width:108px;height:108px;border-radius:50%;background:linear-gradient(200deg,#8fa8c2 0%,#9a6a47 45%,#6e3f27 100%)}
</style>
</head>
<body>

<!-- Spread 1: back and front cover -->
<section class="spread spread--cover">
  <article class="page back">
    <div class="back__blob"></div>
    <svg class="back__arcs" width="262" height="300" viewBox="0 0 262 300" aria-hidden="true">
      <path d="M60 40 A125 125 0 0 0 60 260" fill="none" stroke="var(--blue-deep)" stroke-width="12"/>
      <path d="M150 235 A120 120 0 0 0 262 180" fill="none" stroke="var(--blue-deep)" stroke-width="12"/>
      <path d="M180 230 A110 110 0 0 0 262 200" fill="none" stroke="#1d2b4e" stroke-width="6"/>
      <circle cx="166" cy="148" r="98" fill="var(--blue-deep)"/>
      <circle cx="166" cy="148" r="98" fill="none" stroke="var(--white)" stroke-width="3"/>
      <path d="M130 255 a18 18 0 0 1 30 0" fill="var(--mist)"/>
    </svg>
    <div class="benefits">
      <h2 class="benefits__title">BENEFITS:</h2>
      <ul class="benefits__list">
        <li><svg class="tick" viewBox="0 0 10 10"><circle cx="5" cy="5" r="4.5" fill="none" stroke="#6fd18a"/><path d="M2.8 5.2l1.5 1.5 3-3.2" fill="none" stroke="#6fd18a" stroke-width="1.2"/></svg>Boost Curb Appeal Instantly</li>
        <li><svg class="tick" viewBox="0 0 10 10"><circle cx="5" cy="5" r="4.5" fill="none" stroke="#6fd18a"/><path d="M2.8 5.2l1.5 1.5 3-3.2" fill="none" stroke="#6fd18a" stroke-width="1.2"/></svg>Remove Mold, Algae, And Dirt</li>
        <li><svg class="tick" viewBox="0 0 10 10"><circle cx="5" cy="5" r="4.5" fill="none" stroke="#6fd18a"/><path d="M2.8 5.2l1.5 1.5 3-3.2" fill="none" stroke="#6fd18a" stroke-width="1.2"/></svg>Protect Your Property Surfaces</li>
        <li><svg class="tick" viewBox="0 0 10 10"><circle cx="5" cy="5" r="4.5" fill="none" stroke="#6fd18a"/><path d="M2.8 5.2l1.5 1.5 3-3.2" fill="none" stroke="#6fd18a" stroke-width="1.2"/></svg>Improve Property Value</li>
      </ul>
    </div>
    <div class="back__cta">Call Today For A Free Quote</div>
    <p class="back__tagline">Book Your Power Washing Service Now</p>
    <div class="back__phone">
      <svg viewBox="0 0 24 24" aria-hidden="true"><path d="M6.6 10.8a15 15 0 0 0 6.6 6.6l2.2-2.2a1 1 0 0 1 1-.25 11.4 11.4 0 0 0 3.6.57 1 1 0 0 1 1 1V20a1 1 0 0 1-1 1A17 17 0 0 1 3 4a1 1 0 0 1 1-1h3.5a1 1 0 0 1 1 1c0 1.25.2 2.45.57 3.57a1 1 0 0 1-.25 1z" fill="var(--ink)"/></svg>
      201-555-0148
    </div>
    <div class="brand">HARBORLINE PRESSURE WASHING</div>
  </article>

  <article class="page front">
    <h1 class="headline front__title">Boost Your Home’s Curb Appeal</h1>
    <div class="front__rule"></div>
    <div class="brand">HARBORLINE PRESSURE WASHING</div>
    <div class="photo before-after">
      <div class="before-after__half before-after__half--before" role="img" aria-label="Brick driveway and garage door before pressure washing"><span class="tag tag--before">Before</span></div>
      <div class="before-after__half before-after__half--after" role="img" aria-label="Same brick driveway and garage door after pressure washing"><span class="tag tag--after">After</span></div>
    </div>
    <div class="front__panel">
      <h2 class="headline front__panel-title">Professional Exterior Cleaning Services</h2>
      <p class="front__panel-text">Professional Exterior Cleaning Removes Dirt, Stains, And Grime, Restoring Surfaces Beautifully.</p>
      <div class="front__button">Get A Free Quote Today</div>
      <svg class="front__stripes" width="70" height="90" viewBox="0 0 70 90" aria-hidden="true">
        <path d="M20 62 L70 8 M8 78 L70 22 M30 90 L70 48" stroke="var(--white)" stroke-width="2"/>
        <path d="M70 55 L70 90 L36 90 Z" fill="var(--white)"/>
      </svg>
    </div>
  </article>
</section>

<!-- Spread 2: services inside -->
<section class="spread spread--services">
  <article class="page services">
    <h2 class="services__title">OUR SERVICES</h2>
    <p class="services__intro">Professional Pressure Washing Removes Dirt, Grime, And Stains From Homes, Businesses, Driveways, Patios, And Tennis Courts, Restoring Clean, Fresh Surfaces.</p>

    <div class="service" style="top:102px">
      <div class="photo service__photo" role="img" aria-label="Worker washing a glass storefront" style="background:linear-gradient(160deg,#4f7fa8,#9cc4d9 60%,#3f6a3a)"></div>
      <div><h3 class="service__name">Residential &amp; Commercial Washing</h3><p class="service__text">Residential And Commercial Pressure Washing Removes Dirt, Stains, And Mold, Keeping Properties Clean, Fresh, And Well-Maintained.</p></div>
    </div>
    <div class="service__rule" style="top:175px"></div>

    <div class="service" style="top:184px">
      <div class="photo service__photo" role="img" aria-label="Worker pressure washing a concrete sidewalk" style="background:linear-gradient(160deg,#3d6a8c,#8fb0c4 50%,#c9c2b2)"></div>
      <div><h3 class="service__name">Driveways, Sidewalks &amp; Concrete Cleaning</h3><p class="service__text">Professional Cleaning Removes Dirt, Oil Stains, And Grime From Driveways, Sidewalks, And Concrete Surfaces, Restoring Their Appearance.</p></div>
    </div>
    <div class="service__rule" style="top:256px"></div>

    <div class="service" style="top:268px">
      <div class="photo service__photo" role="img" aria-label="Stone paver patio" style="background:linear-gradient(160deg,#d9d6cf,#a9a59a 60%,#7f8b6c)"></div>
      <div><h3 class="service__name">Decks, Patios &amp; Paver Restoration</h3><p class="service__text">Restoring Decks, Patios, And Pavers By Removing Stains, Dirt, And Buildup.</p></div>
    </div>
    <div class="service__rule" style="top:340px"></div>

    <div class="service" style="top:351px">
      <div class="photo service__photo" role="img" aria-label="Outdoor tennis court surface" style="background:linear-gradient(160deg,#5e9ab8,#2f7c8f 55%,#4a8a5c)"></div>
      <div><h3 class="service__name">Tennis Courts &amp; Specialty Surface Cleaning</h3><p class="service__text">Professional Cleaning For Tennis Courts And Specialty Surfaces Removes Dirt, Stains, And Buildup.</p></div>
    </div>
  </article>

  <article class="page features">
    <div class="feature feature--driveway">
      <h3 class="headline feature__label" style="left:16px;top:55px">Driveway Cleaning</h3>
      <div class="photo feature__photo" role="img" aria-label="Paved driveway before and after cleaning"></div>
    </div>
    <div class="feature feature--deck">
      <div class="deck__ring"></div>
      <div class="photo deck__photo" role="img" aria-label="Restored wooden deck"></div>
      <h3 class="headline feature__label" style="left:160px;top:56px">Deck Restoration</h3>
    </div>
    <div class="feature feature--concrete">
      <h3 class="headline feature__label" style="left:20px;top:55px">Concrete Cleaning</h3>
      <div class="photo feature__photo" role="img" aria-label="Freshly cleaned concrete walkway"></div>
    </div>
  </article>
</section>

</body>
</html>
```